Business Card Design - ThriveMetric

Looking for creative, modern design, two sided for ThriveMetric that is consistent with color and feel of website www.thrivemetric.net.

Back of card will be used to promote products or have a quote revolving around decisions, change, leadership, innovation, creativity. Back should also have space to promote website, but optional to use the icon. Front of the card will need to use the icon and have standard place for name, job title, phone and email. We are not looking to put a mailing address or fax. Also want space to place a few words/phrase explaining what we do...such as individual growth and organizational development or tools, training, information...in addition, want the linkpage icon small on the front somewhere as we are also on linkpage.

Vector file uploaded of icon.

Target Market(s)

Professional coaching for individual growth and organizational development

Industry/Entity Type

Business

Requirements
Must have
• Icon...see attached.

```html
<!DOCTYPE html>
<html lang="en">
<head>
<meta charset="utf-8">
<title>ThriveMetric Business Card</title>
<link href="https://fonts.googleapis.com/css2?family=Open+Sans:wght@300;400;600;700&display=swap" rel="stylesheet">
<style>
  :root {
    --page-bg: #e4e6ea;
    --brand-blue: #1f4f9e;
    --brand-blue-deep: #173f84;
    --brand-blue-light: #2d66b8;
    --sky: #5fb4ec;
    --card-white: #f7f8fb;
    --ink-blue: #24509a;
    --soft-white: rgba(255,255,255,0.85);
  }
  * { box-sizing: border-box; margin: 0; padding: 0; }
  html, body { width: 1200px; height: 900px; overflow: hidden; }
  body {
    background: var(--page-bg);
    font-family: "Open Sans", Arial, sans-serif;
    display: flex;
    align-items: center;
    justify-content: center;
    gap: 40px;
  }
  .card {
    position: relative;
    width: 540px;
    height: 309px;
    border-radius: 4px;
    overflow: hidden;
    box-shadow: 0 6px 18px rgba(0,0,0,0.18);
  }

  /* Back side */
  .card-back {
    background: linear-gradient(135deg, var(--brand-blue-light) 0%, var(--brand-blue) 55%, var(--brand-blue-deep) 100%);
    color: #fff;
  }
  .card-back .brand-dot {
    position: absolute;
    left: 48px;
    top: 92px;
    width: 120px;
    height: 120px;
    border-radius: 50%;
    background: var(--sky);
  }
  .card-back .back-text {
    position: absolute;
    left: 196px;
    top: 88px;
    right: 30px;
  }
  .card-back .brand-name {
    font-weight: 300;
    font-size: 44px;
    line-height: 1.05;
    letter-spacing: -0.5px;
  }
  .card-back .brand-url {
    font-size: 14px;
    font-weight: 400;
    margin-top: 6px;
    color: var(--soft-white);
  }
  .card-back .brand-pitch {
    font-size: 13px;
    font-weight: 400;
    line-height: 1.45;
    margin-top: 18px;
    color: var(--soft-white);
  }

  /* Front side */
  .card-front {
    background: var(--card-white);
    color: var(--ink-blue);
  }
  .card-front .edge-band {
    position: absolute;
    top: 0;
    right: 0;
    width: 30px;
    height: 100%;
    background: var(--brand-blue);
  }
  .card-front .identity {
    position: absolute;
    left: 30px;
    top: 34px;
    display: flex;
    align-items: center;
    gap: 14px;
  }
  .card-front .identity .brand-dot {
    width: 58px;
    height: 58px;
    border-radius: 50%;
    background: var(--sky);
    flex: none;
  }
  .card-front .brand-name {
    font-weight: 400;
    font-size: 30px;
    line-height: 1;
    letter-spacing: -0.3px;
  }
  .card-front .brand-tagline {
    font-size: 10.5px;
    margin-top: 5px;
  }
  .card-front .person {
    position: absolute;
    left: 30px;
    bottom: 34px;
  }
  .card-front .person-name {
    font-weight: 700;
    font-size: 19px;
    line-height: 1.1;
  }
  .card-front .person-role {
    font-size: 13px;
    margin-top: 2px;
  }
  .card-front .social {
    display: flex;
    align-items: center;
    gap: 6px;
    font-size: 13px;
    margin-top: 8px;
  }
  .card-front .social-dot {
    width: 13px;
    height: 13px;
    border-radius: 50%;
    background: var(--ink-blue);
  }
  .card-front .contact-list {
    position: absolute;
    right: 56px;
    bottom: 38px;
    list-style: none;
    font-size: 13px;
  }
  .card-front .contact-list li {
    display: flex;
    align-items: center;
    gap: 7px;
    margin-top: 5px;
  }
  .card-front .contact-icon {
    width: 14px;
    height: 14px;
    border-radius: 3px;
    background: var(--ink-blue);
    display: flex;
    align-items: center;
    justify-content: center;
  }
</style>
</head>
<body>

  <section class="card card-back" aria-label="Card back">
    <div class="brand-dot"></div>
    <div class="back-text">
      <h1 class="brand-name">ThriveMetric</h1>
      <p class="brand-url">www.thrivemetric.net</p>
      <p class="brand-pitch">Providing tools, training, information and<br>collaboration to achieve the results you want.</p>
    </div>
  </section>

  <section class="card card-front" aria-label="Card front">
    <div class="edge-band"></div>
    <div class="identity">
      <div class="brand-dot"></div>
      <div>
        <h2 class="brand-name">ThriveMetric</h2>
        <p class="brand-tagline">Supporting Individual Growth &amp; Organizational Development</p>
      </div>
    </div>

    <div class="person">
      <p class="person-name">Marcus Ellery</p>
      <p class="person-role">Position</p>
      <p class="social"><span class="social-dot"></span>/thrivemetric</p>
    </div>

    <ul class="contact-list">
      <li>
        <span class="contact-icon">
          <svg width="10" height="10" viewBox="0 0 10 10"><path d="M2.2 1h1.6l.7 2-1 .8a5 5 0 0 0 2.7 2.7l.8-1 2 .7v1.6c0 .5-.4.9-.9.9A7.4 7.4 0 0 1 1.3 1.9c0-.5.4-.9.9-.9z" fill="#fff"/></svg>
        </span>1.800.555.0147
      </li>
      <li>
        <span class="contact-icon">
          <svg width="10" height="10" viewBox="0 0 10 10"><rect x="1" y="2.2" width="8" height="5.6" rx="0.6" fill="none" stroke="#fff" stroke-width="1"/><path d="M1.3 2.6 5 5.4l3.7-2.8" fill="none" stroke="#fff" stroke-width="1"/></svg>
        </span>contact@thrivemetric.net
      </li>
      <li>
        <span class="contact-icon">
          <svg width="10" height="10" viewBox="0 0 10 10"><circle cx="5" cy="5" r="3.8" fill="none" stroke="#fff" stroke-width="0.9"/><ellipse cx="5" cy="5" rx="1.6" ry="3.8" fill="none" stroke="#fff" stroke-width="0.8"/><path d="M1.2 5h7.6" stroke="#fff" stroke-width="0.8"/></svg>
        </span>www.thrivemetric.net
      </li>
    </ul>
  </section>

</body>
</html>
```